Corvella Sign

Design a sign for Pizza and Pasta restaurant in New Jersey
Black background
Size = 120" w x 23.5" h
Corvella - top line
Brick Oven Pizza & Pasta - second line

Target Market(s)

everybody

Industry/Entity Type

restaurant

Font styles to use
Decorative
Script

Colors

Designer to choose only greyscale colors for use in the design.

Requirements
Must have
• Brick Oven Pizza & Pasta
Nice to have
• Vector file

```html
<!DOCTYPE html>
<html lang="en">
<head>
<meta charset="utf-8">
<title>Corvella Sign</title>
<link rel="stylesheet" href="https://fonts.googleapis.com/css2?family=Allura&family=Josefin+Sans:wght@300;400&display=swap">
<style>
  :root {
    --page: #e6e6e4;
    --sign: #3c4046;
    --ink: #f4f4f2;
    --sketch-light: #8a8e94;
    --sketch-dark: #565a60;
  }
  * { margin: 0; padding: 0; box-sizing: border-box; }
  html, body {
    width: 1200px;
    height: 738px;
    overflow: hidden;
    background: var(--page);
  }
  .canvas {
    position: relative;
    width: 1200px;
    height: 738px;
  }
  .sign {
    position: absolute;
    left: 20px;
    top: 256px;
    width: 1160px;
    height: 227px;
    background: var(--sign);
    overflow: hidden;
  }
  .pizza-art {
    position: absolute;
    left: 0;
    top: 0;
    width: 280px;
    height: 227px;
    background: radial-gradient(circle at 30% 55%, var(--sketch-light), var(--sketch-dark) 75%, var(--sign));
  }
  .pasta-art {
    position: absolute;
    right: 0;
    top: 55px;
    width: 130px;
    height: 172px;
    background: radial-gradient(circle at 55% 55%, var(--sketch-light), var(--sketch-dark) 70%, var(--sign));
  }
  .rules {
    position: absolute;
    inset: 0;
  }
  .brand-name {
    position: absolute;
    left: 470px;
    top: 28px;
    font-family: "Allura", cursive;
    font-weight: 400;
    font-size: 130px;
    line-height: 1;
    color: var(--ink);
    white-space: nowrap;
  }
  .tagline {
    position: absolute;
    font-family: "Josefin Sans", sans-serif;
    font-weight: 300;
    color: var(--ink);
    text-transform: uppercase;
    letter-spacing: 7px;
    line-height: 1;
    white-space: nowrap;
  }
  .tagline-oven {
    left: 330px;
    top: 146px;
    font-size: 26px;
  }
  .tagline-menu {
    left: 690px;
    top: 182px;
    font-size: 24px;
  }
</style>
</head>
<body>
  <main class="canvas">
    <section class="sign">
      <div class="pizza-art" role="img" aria-label="White line sketch of a sliced pizza topped with basil, mozzarella and olives"></div>
      <div class="pasta-art" role="img" aria-label="White line sketch of assorted pasta shapes: farfalle, rigatoni and penne"></div>

      <svg class="rules" width="1160" height="227" viewBox="0 0 1160 227" aria-hidden="true">
        <g stroke="#f4f4f2" stroke-width="1.4" fill="none">
          <line x1="285" y1="18" x2="1000" y2="18"/>
          <line x1="300" y1="180" x2="610" y2="180"/>
          <line x1="660" y1="214" x2="1020" y2="214"/>
        </g>
      </svg>

      <h1 class="brand-name">Corvella</h1>
      <p class="tagline tagline-oven">Brick Oven</p>
      <p class="tagline tagline-menu">Pizza &amp; Pasta</p>
    </section>
  </main>
</body>
</html>
```